Natural Sunscreen Label Design for a Natural Cosmetics brand

We are looking to create a label design for a Natural Sunscreen Lotion. The labels will be a stick-on label on a white background tube. Enclosed a file with the content and some ideas/references. Please feel free to explore more.

It is important that the SPF is highlighted as large text and to use colors that give the customer an impression this being a sunscreen from far away as well.
We like white and orange/amber/yellow.
Details attached
Our Logo is attached as well as the size template of the label.

```html
<!DOCTYPE html>
<html lang="en">
<head>
<meta charset="utf-8">
<title>Brisa Mar Natural Sun Lotion Label</title>
<link href="https://fonts.googleapis.com/css2?family=Montserrat:wght@700;800&family=Oswald:wght@300;400&family=Josefin+Sans:wght@400;600&display=swap" rel="stylesheet">
<style>
  :root {
    --bg: #f1f1ef;
    --label: #ffffff;
    --orange: #f39a2c;
    --orange-light: #f8b563;
    --amber: #f7a21b;
    --grey: #8a8a8a;
    --grey-dark: #3d3d3d;
    --grey-light: #b4b4b4;
    --green: #6ab04c;
    --white: #ffffff;
  }
  html, body {
    margin: 0;
    width: 1200px;
    height: 1200px;
    overflow: hidden;
    background: var(--bg);
  }
  .label {
    position: absolute;
    left: 110px;
    top: 260px;
    width: 980px;
    height: 680px;
    background: var(--label);
    box-shadow: 0 6px 30px rgba(0,0,0,0.08);
  }
  .spf-panel {
    position: absolute;
    left: 0; top: 0;
    width: 340px; height: 100%;
    background: linear-gradient(135deg, var(--orange-light) 0%, var(--orange) 45%, var(--amber) 100%);
    color: var(--white);
    font-family: "Montserrat", sans-serif;
  }
  .brand-mark {
    position: absolute;
    left: 44px; top: 56px;
    display: flex; align-items: center; gap: 14px;
    font-family: "Josefin Sans", sans-serif;
    font-weight: 600;
    font-size: 22px;
    letter-spacing: 3px;
    text-transform: uppercase;
    color: var(--white);
    line-height: 1.2;
  }
  .brand-mark .dot {
    width: 46px; height: 46px; border-radius: 50%;
    border: 2px solid var(--white);
    flex: none;
  }
  .spf-value {
    position: absolute; left: 36px; top: 250px;
    font-size: 128px; font-weight: 800; line-height: 0.95;
    letter-spacing: -2px;
  }
  .spf-value span { display: block; }
  .spf-rays {
    position: absolute; left: 40px; top: 520px;
    font-size: 46px; font-weight: 800; letter-spacing: 1px;
  }
  .spf-volume {
    position: absolute; left: 62px; top: 598px;
    font-family: "Oswald", sans-serif; font-weight: 400;
    font-size: 42px;
  }
  .content {
    position: absolute; left: 400px; top: 40px; right: 40px;
  }
  .product-name {
    font-family: "Josefin Sans", sans-serif;
    font-weight: 600;
    font-size: 110px;
    line-height: 1;
    color: var(--orange);
    letter-spacing: 6px;
    margin: 20px 0 0;
  }
  .product-name .line { display: block; }
  .subtitle {
    font-family: "Oswald", sans-serif; font-weight: 300;
    font-size: 46px; color: var(--grey);
    margin: 36px 0 0 40px; line-height: 1.2;
  }
  .usage {
    font-family: "Oswald", sans-serif;
    font-size: 30px; margin: 24px 0 0 10px;
    display: flex; gap: 28px;
  }
  .usage .en { color: var(--grey); font-weight: 300; }
  .usage .pt { color: var(--grey-dark); font-weight: 400; }
  .claims {
    display: flex; align-items: center; gap: 20px;
    margin: 22px 0 0 10px;
  }
  .claims-text {
    font-family: "Oswald", sans-serif; font-weight: 300;
    font-size: 19px; color: var(--grey-light);
    text-align: center; line-height: 1.35;
  }
  .claims-text p { margin: 0 0 14px; }
  .badge {
    width: 46px; height: 46px; border-radius: 50%;
    border: 3px solid var(--green); flex: none;
  }
</style>
</head>
<body>
  <div class="label">
    <div class="spf-panel">
      <div class="brand-mark"><span class="dot"></span>Costa Viva<br>Portugal</div>
      <div class="spf-value"><span>30+</span><span>SPF</span></div>
      <div class="spf-rays">UVA/UVB</div>
      <div class="spf-volume">℮100ml</div>
    </div>
    <div class="content">
      <h1 class="product-name">
        <span class="line">BRISA</span>
        <span class="line">MAR</span>
      </h1>
      <div class="subtitle">Natural Sun Lotion<br>Loção Solar Natural</div>
      <div class="usage"><span class="en">For Body and Face</span><span class="pt">Para corpo e rosto</span></div>
      <div class="claims">
        <div class="claims-text">
          <p>With BIO Aloe Vera, Non-greasy, Water Resistant,<br>Safe for kids and adults</p>
          <p>Com BIO Aloe Vera, não gorduroso, resistente à<br>água, seguro para crianças e adultos</p>
        </div>
        <span class="badge" role="img" aria-label="Vegan certification badge"></span>
      </div>
    </div>
  </div>
</body>
</html>
```